Flyer für Hersteller von Spiegeln
Zielgruppe
Wir stellen hochwertige Spiegel - beleuchtet und unbeleuchtet - her. Der Vertrieb erfolgt überwiegend online. https://www.lumvaro-glas.com/ Jetzt brauchen wir für folgenden Artikel einen ansprechenden Flyer: https://www.lumvaro-glas.com/Mikrofasertuch-mit-Naturfasern
Aufgabenstellung
Das Design soll ansprechend sein und das hochwertige Mikrofasertuch und unsere hochwertigen Spiegel hervorrufen.
Unser langjährig getesteter Allrounder in der Glasreinigung - unser Mikrofasertuch mit Naturfasern
Eine Kombination aus hochwertigen Microfasern und Bambus.
Dieser Fasermischung sorgt durch seine besonders feine Struktur für besonders streifen - und fusselfreie Reinigungsergebnisse bei Ihrem Spiegel.
empfehlung zur Reinigung Ihrer Spiegel
kann zur Reinigung Ihrer Fenster eingesetzt werden
kann zur Reinigung von großen Glasflächen eingesetzt werden
kann als Poliertuch für Gläser eingesetzt werden
Microfasertuch mit Bambusfasern - besonders fein strukturiert und umweldverträglich
besonders umweltfreundlich durch nachwachsenden Bambus
enthält einen hohen Anteil an Bambusfasern
streifenfreie Glasreinigung / fusselfreie Spiegelreinigung
besonders schonend zu Ihrem neuen Spiegel
perfekte & von uns lange getestete Alternative zu herkömmlichen Microfasertüchern
waschbar bei maximal 60°C (ohne Weichspüler)
40 x 45 cm
17% Bambus, 17% Polyamid-Mikrofaser, 66% Polyester-Microfaser
Zertifiziert nach ISO 9001, Reach, Vera-Fil

```html
<!DOCTYPE html>
<html lang="de">
<head>
<meta charset="utf-8">
<title>Mikrofasertuch mit Naturfasern – Flyer</title>
<link rel="stylesheet" href="https://fonts.googleapis.com/css2?family=Bebas+Neue&family=Oswald:wght@500;600&family=Roboto:wght@400&display=swap">
<style>
  :root {
    --orange: #f29100;
    --dark: #2f2f2f;
    --white: #ffffff;
    --text: #2b2b2b;
    --bg-light: #f5f8fa;
    --bg-edge: #dfe2e4;
    --cloth: #a8c83a;
    --cloth-dark: #8fae2a;
  }
  html, body { margin: 0; padding: 0; overflow: hidden; }
  .flyer {
    position: relative;
    width: 848px; height: 1200px; overflow: hidden;
    background: radial-gradient(ellipse at 50% 45%, var(--bg-light) 0%, #eceff1 55%, var(--bg-edge) 100%);
    font-family: "Roboto", Arial, sans-serif;
    color: var(--text);
  }
  .product-visual {
    position: absolute; left: 152px; top: 46px; width: 562px; height: 272px;
    border-radius: 18px 30px 10px 10px;
    background: linear-gradient(160deg, #b8d648 0%, var(--cloth) 50%, var(--cloth-dark) 100%);
    box-shadow: 0 10px 14px rgba(0,0,0,0.18);
  }
  .title-band { position: absolute; left: 0; top: 355px; width: 600px; height: 176px; }
  .title {
    position: absolute; left: 43px; top: 381px; margin: 0;
    font-family: "Bebas Neue", "Oswald", "Arial Narrow", sans-serif; font-weight: 400;
    font-size: 68px; line-height: 65px; color: var(--white);
    text-transform: uppercase; letter-spacing: 0;
    white-space: nowrap;
  }
  .badge-text {
    position: absolute; left: 444px; top: 386px; width: 130px;
    font-family: "Bebas Neue", "Oswald", "Arial Narrow", sans-serif; font-weight: 400;
    font-size: 26px; line-height: 25.5px; color: var(--white);
    text-align: center; text-transform: uppercase;
  }
  .content { position: absolute; left: 42px; top: 552px; width: 780px; }
  .lead-heading {
    margin: 0; font-family: "Oswald", "Arial Narrow", sans-serif; font-weight: 500;
    font-size: 28px; line-height: 34px; color: var(--orange);
  }
  .intro { margin: 5px 0 0; width: 725px; font-size: 19.8px; line-height: 25.6px; }
  .features { list-style: none; margin: 18px 0 0; padding: 0; font-size: 15.9px; line-height: 21.5px; }
  .features li::before { content: "•"; margin-right: 6px; }
  .sub-heading {
    margin: 15px 0 0 -2px; font-family: "Oswald", "Arial Narrow", sans-serif; font-weight: 500;
    font-size: 23.5px; line-height: 28px; color: var(--orange);
  }
  .features.details { margin-top: 12px; }
  .footer-shape { position: absolute; left: 0; top: 1085px; width: 848px; height: 115px; }
  .footer-address {
    position: absolute; left: 20px; top: 1161px;
    font-family: "Oswald", "Arial Narrow", sans-serif; font-weight: 500;
    font-size: 17px; color: var(--white); letter-spacing: 0.1px;
  }
  .footer-web {
    position: absolute; left: 551px; top: 1150px;
    font-family: "Oswald", "Arial Narrow", sans-serif; font-weight: 600;
    font-size: 26px; color: var(--white);
  }
</style>
</head>
<body>
<div class="flyer">
  <div class="product-visual" role="img" aria-label="Produktfoto: gefaltetes grünes Mikrofasertuch mit weißen Streifen"></div>

  <svg class="title-band" viewBox="0 0 600 176" aria-hidden="true">
    <path d="M0 0 H510 A88 88 0 0 1 510 176 H0 Z" fill="var(--orange)"/>
    <circle cx="509" cy="88" r="77" fill="var(--white)"/>
    <circle cx="509" cy="88" r="69" fill="var(--dark)"/>
  </svg>
  <h1 class="title">Mikrofasertuch<br>mit Naturfasern</h1>
  <div class="badge-text">Der<br>Allrounder<br>in der Glas-<br>reinigung</div>

  <main class="content">
    <h2 class="lead-heading">Unser langjährig getesteter Allrounder in der Glasreinigung -<br>unser Mikrofasertuch mit Naturfasern</h2>
    <p class="intro">Eine Kombination aus hochwertigen Microfasern und Bambus.<br>Dieser Fasermischung sorgt durch seine besonders feine Struktur für besonders streifen - und fusselfreie Reinigungsergebnisse bei Ihrem Spiegel.</p>
    <ul class="features">
      <li>Empfehlung zur Reinigung Ihrer Spiegel</li>
      <li>kann zur Reinigung Ihrer Fenster eingesetzt werden</li>
      <li>kann zur Reinigung von großen Glasflächen eingesetzt werden</li>
      <li>kann als Poliertuch für Gläser eingesetzt werden</li>
    </ul>
    <h2 class="sub-heading">Microfasertuch mit Bambusfasern -<br>besonders fein strukturiert und umweldverträglich</h2>
    <ul class="features details">
      <li>besonders umweltfreundlich durch nachwachsenden Bambus</li>
      <li>enthält einen hohen Anteil an Bambusfasern</li>
      <li>streifenfreie Glasreinigung / fusselfreie Spiegelreinigung</li>
      <li>besonders schonend zu Ihrem neuen Spiegel</li>
      <li>perfekte &amp; von uns lange getestete Alternative zu herkömmlichen Microfasertüchern</li>
      <li>waschbar bei maximal 60°C (ohne Weichspüler)</li>
      <li>40 x 45 cm</li>
      <li>17% Bambus, 17% Polyamid-Mikrofaser, 66% Polyester-Microfaser</li>
      <li>Zertifiziert nach ISO 9001, Reach, Vera-Fil</li>
    </ul>
  </main>

  <svg class="footer-shape" viewBox="0 0 848 115" aria-hidden="true">
    <path d="M0 61 H370 C420 61 430 6 480 6 H848 V115 H0 Z" fill="var(--dark)"/>
    <path d="M516 115 V72 A30 30 0 0 1 546 42 H848 V115 Z" fill="var(--white)"/>
    <path d="M520 115 V74 A28 28 0 0 1 548 46 H848 V115 Z" fill="var(--orange)"/>
  </svg>
  <div class="footer-address">Lumvaro Glas-Design-GmbH &nbsp;|&nbsp; Kesselweg 4-6 &nbsp;|&nbsp; 32190 Hallfeld</div>
  <div class="footer-web">www.lumvaro-glas.com</div>
</div>
</body>
</html>
```